Product label for premium fruit wooden crates

Background: KelVaro offers premium quality fruits airflown (i.e. Japan, USA, Australia, etc) to Singapore at an affordable price. This includes exquisite and limited fruits like Shine Muscat grape, Shizuoka Crown Melon, Yellow Dragon Fruit, Fei zi xiao seedless lychee, Yellow Peaches, etc.

Requirements:

- Design a premium fruit’s label strap for identification and brand marketing.

- This strap will be used to tie around our fruit gift crate and fruit boxes (see attached).

- the logo use in this strap may use different color that must fit the 2 ribbons that will be used together with the crate box (see attached), red and gold ribbons(purl satin)

- the fruit crates and boxes will be presented as gift for vip, families, and working partners (important people)

This label will be printed in paper and tie around the fruit crate or paper box.

Web: www.kelvaro.sg
FB: https://www.facebook.com/kvrorch/
IG: https://www.instagram.com/kvrorch

Target Market(s)

Working class, families, expat, business clients (late 20 – 40s)

Industry/Entity Type

Gift Shop

Font styles to use
Other font styles liked:
• Sakkal Majalla

Requirements
Must have
• - color that fit the 2 ribbons color (red and gold)
• - premium, luxury and exquisite feel
• - presentable as a gift to someone important
• - Kelvaro's logo
• - The word 'KELVARO',
Nice to have
• the following words:
• - www.kelvaro.sg; or/and
• - online premium fruits or/and
• - premium quality (No preference. let the designer choose)
• must be able to give customer a feel that Kelvaro sells premium fruits
Should not have
• cant think of it now

```html
<!DOCTYPE html>
<html lang="en">
<head>
<meta charset="utf-8">
<title>KelVaro Premium Fruit Crate Strap</title>
<link rel="stylesheet" href="https://fonts.googleapis.com/css2?family=Questrial&family=Playfair+Display:ital,wght@1,700&family=Libre+Baskerville:ital,wght@1,700&display=swap">
<style>
  :root {
    --page: #ffffff;
    --band-light: #fdf8cf;
    --band-mid: #f5ea98;
    --band-deep: #ecd96a;
    --rim-pink: #ea8f95;
    --rim-rose: #f3b3b3;
    --rim-dark: #9e1c28;
    --ring-green-dark: #4f8233;
    --ring-green-light: #a9c56d;
    --ring-cream: #fbf3bf;
    --ribbon-main: #e8646f;
    --ribbon-soft: #f49b8d;
    --ribbon-tail: #d9505f;
    --ribbon-fold: #a82a3a;
    --gold-dark: #8a6417;
    --gold-light: #e6c25a;
    --brand-coral: #e35d6a;
    --text-green: #3f7a2a;
  }
  html, body {
    margin: 0;
    padding: 0;
    width: 1200px;
    height: 750px;
    overflow: hidden;
    background: var(--page);
  }
  .strap-label {
    display: block;
    width: 1200px;
    height: 750px;
  }
  .arc-outer-text {
    font-family: "Questrial", sans-serif;
    font-size: 19px;
    fill: var(--text-green);
  }
  .arc-ring-text {
    font-family: "Libre Baskerville", serif;
    font-style: italic;
    font-weight: 700;
    font-size: 19px;
    letter-spacing: 3px;
    fill: var(--ring-cream);
    stroke: var(--ring-green-dark);
    stroke-width: 0.6px;
  }
  .ribbon-title {
    font-family: "Playfair Display", serif;
    font-style: italic;
    font-weight: 700;
    font-size: 36px;
    fill: url(#goldText);
  }
  .brand-word {
    font-family: "Questrial", sans-serif;
    font-size: 20px;
    letter-spacing: 1px;
    fill: var(--brand-coral);
  }
  .brand-mark-name {
    font-family: "Questrial", sans-serif;
    font-size: 22px;
    fill: var(--brand-coral);
  }
</style>
</head>
<body>
<svg class="strap-label" viewBox="0 0 800 500" xmlns="http://www.w3.org/2000/svg" aria-label="KelVaro premium fruit crate strap label">
  <defs>
    <linearGradient id="bandFill" x1="0" y1="0" x2="1" y2="0">
      <stop offset="0" stop-color="var(--band-deep)"/>
      <stop offset="0.3" stop-color="var(--band-light)"/>
      <stop offset="0.7" stop-color="var(--band-mid)"/>
      <stop offset="1" stop-color="var(--band-light)"/>
    </linearGradient>
    <linearGradient id="rimFill" x1="0" y1="0" x2="0" y2="1">
      <stop offset="0" stop-color="var(--rim-rose)"/>
      <stop offset="0.5" stop-color="var(--rim-pink)"/>
      <stop offset="1" stop-color="var(--rim-rose)"/>
    </linearGradient>
    <linearGradient id="ringFill" x1="0" y1="0" x2="1" y2="1">
      <stop offset="0" stop-color="var(--ring-green-light)"/>
      <stop offset="0.5" stop-color="var(--ring-green-dark)"/>
      <stop offset="1" stop-color="var(--ring-green-light)"/>
    </linearGradient>
    <radialGradient id="centreFill" cx="0.5" cy="0.45" r="0.6">
      <stop offset="0" stop-color="#fffbe0"/>
      <stop offset="1" stop-color="var(--band-mid)"/>
    </radialGradient>
    <linearGradient id="ribbonFill" x1="0" y1="0" x2="1" y2="0">
      <stop offset="0" stop-color="var(--ribbon-main)"/>
      <stop offset="0.5" stop-color="var(--ribbon-soft)"/>
      <stop offset="1" stop-color="var(--ribbon-main)"/>
    </linearGradient>
    <linearGradient id="goldText" x1="0" y1="0" x2="0" y2="1">
      <stop offset="0" stop-color="var(--gold-light)"/>
      <stop offset="1" stop-color="var(--gold-dark)"/>
    </linearGradient>

    <path id="outerTopArc" d="M 232 238 A 168 168 0 0 1 568 238"/>
    <path id="outerBottomArc" d="M 212 238 A 188 188 0 0 0 588 238"/>
    <path id="ringTopArc" d="M 263 238 A 137 137 0 0 1 537 238"/>
    <path id="ringBottomArc" d="M 249 238 A 151 151 0 0 0 551 238"/>
    <path id="ribbonMid" d="M 200 268 Q 400 326 600 268"/>
  </defs>

  <!-- strap rim layer -->
  <g class="strap-rim">
    <rect x="30" y="128" width="740" height="230" fill="url(#rimFill)"/>
    <rect x="30" y="128" width="12" height="230" fill="var(--rim-dark)"/>
    <rect x="758" y="128" width="12" height="230" fill="var(--rim-dark)"/>
    <circle cx="400" cy="240" r="230" fill="url(#rimFill)"/>
  </g>

  <!-- strap face layer -->
  <g class="strap-face">
    <rect x="42" y="137" width="716" height="212" fill="url(#bandFill)"/>
    <circle cx="400" cy="240" r="221" fill="url(#bandFill)"/>
  </g>

  <!-- seal ring -->
  <g class="seal">
    <circle cx="400" cy="238" r="160" fill="url(#ringFill)"/>
    <circle cx="400" cy="238" r="126" fill="url(#centreFill)" stroke="var(--ring-green-dark)" stroke-width="2"/>
  </g>

  <!-- arc texts -->
  <text class="arc-outer-text"><textPath href="#outerTopArc" startOffset="50%" text-anchor="middle">Online Premium Fruits with Premium Quality</textPath></text>
  <text class="arc-outer-text" font-size="20"><textPath href="#outerBottomArc" startOffset="50%" text-anchor="middle">www.kelvaro.sg</textPath></text>
  <text class="arc-ring-text"><textPath href="#ringTopArc" startOffset="50%" text-anchor="middle">Natural &amp; Fresh</textPath></text>
  <text class="arc-ring-text"><textPath href="#ringBottomArc" startOffset="50%" text-anchor="middle">100% Imported</textPath></text>

  <!-- brand name with plain circle -->
  <g class="brand-mark">
    <circle cx="400" cy="168" r="24" fill="var(--brand-coral)"/>
    <text class="brand-mark-name" x="400" y="220" text-anchor="middle">KelVaro</text>
  </g>

  <!-- ribbon banner -->
  <g class="ribbon-banner">
    <polygon class="ribbon-tail-left" points="95,208 235,208 235,292 95,292 130,250" fill="var(--ribbon-tail)"/>
    <polygon class="ribbon-tail-right" points="705,208 565,208 565,292 705,292 670,250" fill="var(--ribbon-tail)"/>
    <polygon class="ribbon-fold-left" points="200,222 235,208 235,292 200,300" fill="var(--ribbon-fold)"/>
    <polygon class="ribbon-fold-right" points="600,222 565,208 565,292 600,300" fill="var(--ribbon-fold)"/>
    <path class="ribbon-front" d="M 200 222 Q 400 282 600 222 L 600 302 Q 400 362 200 302 Z" fill="url(#ribbonFill)"/>
    <text class="ribbon-title" dy="12"><textPath href="#ribbonMid" startOffset="50%" text-anchor="middle">Premium Quality</textPath></text>
  </g>

  <text class="brand-word" x="400" y="355" text-anchor="middle">KELVARO</text>
</svg>
</body>
</html>
```